Improve Design and Readability of Existing Web Page

Corvantia.org is a free educational radiology resource with one of the web's largest collections of radiology cases and reference articles. This job involves improving the design of the article pages to make the text more readable.
We want a new design for the body of the article page that has considered at least: the typeface, vertical rhythm, line length, line height and styling of the text, headings and other standard HTML elements. IMPORTANT: You would only be designing the content area of the page, inside the existing layout, as indicated here: http://q.zx/i/Tk4W
If you are the successful applicant you'll have your work featured across the 6000+ article pages on the site.
The HTML elements that you will need to consider in your design are:
* Headings (three levels)
* Paragraphs
* Superscript and Subscript text
* Ordered and unordered lists, potentially nested multiple levels deep
* Links to other corvantia content (blue links)
* Links to other corvantia content that does not yet exist (grey links)
The articles are accessible at: http://corvantia.org/encyclopaedia/all/all
Sample articles that can be used for reference and as a base for the redesign:
* http://corvantia.org/articles/neurosarcoidosis
* http://corvantia.org/articles/golden_s_sign
* http://corvantia.org/articles/fetal-heart-rate
* http://corvantia.org/articles/meningioma

```html
<!DOCTYPE html>
<html lang="en">
<head>
<meta charset="utf-8">
<title>Neurosarcoidosis – Corvantia.org</title>
<link href="https://fonts.googleapis.com/css2?family=Source+Sans+3:wght@400;600;700&family=Arimo:wght@400;700&display=swap" rel="stylesheet">
<style>
:root{
  --page-dark:#1f2326;
  --header-top:#1b2a4e;
  --header-bottom:#4a5a92;
  --nav-tab:#2e3f7c;
  --nav-tab-alt:#3a4d8e;
  --content-bg:#ffffff;
  --sidebar-bg:#e4e4e4;
  --title-blue:#27457a;
  --link-blue:#2f6fb3;
  --link-grey:#8c8c8c;
  --heading-purple:#6a3b7c;
  --text:#3a3a3a;
  --rule:#dcdcdc;
  --panel-dark:#24325a;
  --orange:#f08a24;
  --ad-yellow:#f4d21e;
  --ad-red:#e3262b;
}
*{box-sizing:border-box;margin:0;padding:0}
html,body{width:726px;height:1200px;overflow:hidden}
body{position:relative;background:var(--page-dark);font-family:"Source Sans 3",sans-serif;color:var(--text)}
a{text-decoration:none;color:var(--link-blue)}
.abs{position:absolute}

/* header */
.site-header{left:0;top:0;width:726px;height:198px;background:linear-gradient(180deg,var(--header-top),#2c3b6e 60%,var(--header-bottom))}
.brand{left:16px;top:22px;display:flex;align-items:center;gap:6px;color:#fff;font-family:"Arimo",sans-serif;font-weight:700;font-size:21px}
.brand .mark{width:16px;height:16px;border-radius:50%;background:#4a7be0}
.network{left:197px;top:38px;color:#e6e9f3;font-family:"Arimo",sans-serif;font-size:10px;display:flex;align-items:center;gap:5px}
.network .mark{width:10px;height:10px;border-radius:50%;background:#fff}
.account{right:42px;top:10px;font-family:"Arimo",sans-serif;font-size:8px;color:#d3d8e8}
.ad-banner{left:96px;top:74px;width:536px;height:66px;background:#050505;border:1px solid #333}
.ad-banner .co{left:16px;top:16px;color:var(--ad-red);font-family:"Arimo",sans-serif;font-weight:700;font-size:15px}
.ad-banner .tag{left:16px;top:34px;color:#fff;font-family:"Arimo",sans-serif;font-weight:700;font-size:8px}
.ad-banner .art{left:160px;top:2px;width:64px;height:62px;background:linear-gradient(180deg,#3a3f52,#1b4cb5 70%,#101010)}
.ad-banner .head{left:253px;top:4px;color:var(--ad-yellow);font-family:"Arimo",sans-serif;font-style:italic;font-weight:700;font-size:15px;line-height:16px}
.ad-banner .sub{left:253px;top:40px;color:#fff;font-family:"Arimo",sans-serif;font-style:italic;font-size:8px}
.ad-banner .cta{left:253px;top:51px;color:var(--ad-red);font-family:"Arimo",sans-serif;font-style:italic;font-size:7px}
.ads-note{left:571px;top:143px;font-family:"Arimo",sans-serif;font-size:7.5px;color:#c7cde2;text-decoration:underline}

.main-nav{left:16px;top:157px;height:40px;display:flex;font-family:"Arimo",sans-serif;color:#fff}
.main-nav .tab{height:40px;padding:8px 10px;background:var(--nav-tab);border-right:1px solid #4b5c9c}
.main-nav .tab b{display:block;font-size:11px}
.main-nav .tab small{display:block;font-size:6px;color:#8f9ac3;margin-top:2px}
.main-nav .act{display:flex;align-items:center;gap:6px;font-size:8.5px;font-weight:700;line-height:9px;background:var(--nav-tab-alt)}
.main-nav .act i{font-style:normal;font-size:14px}
.gap{width:7px;background:transparent!important;border:0!important;padding:0!important}
.search{left:494px;top:157px;width:215px;height:40px;background:#3f4f88;padding:9px 7px;display:flex;gap:6px}
.search span{flex:1;background:#5b6aa0;border:1px solid #6d7bb0}
.search b{width:44px;background:#222;color:#fff;font-family:"Arimo",sans-serif;font-size:8px;display:flex;align-items:center;justify-content:center;border-radius:2px}

/* content */
.article{left:5px;top:198px;width:421px;height:888px;background:var(--content-bg)}
.sidebar{left:426px;top:198px;width:294px;height:888px;background:var(--sidebar-bg)}
.article-inner{position:absolute;left:19px;top:10px;width:392px}
.article h1{font-weight:400;font-size:21px;color:var(--title-blue);line-height:24px}
.byline{font-size:9px;color:var(--link-blue);margin-top:1px}
hr{border:0;border-top:1px solid var(--rule);margin:10px 0 11px}
.article h2{font-weight:400;font-size:16px;color:var(--heading-purple);margin-bottom:5px}
.article p{font-size:10.8px;line-height:17.6px;margin-bottom:7px}
.article p.lead{width:386px}
.article sup{font-size:6px}
.sym-list{list-style:none;font-size:10px;margin-top:10px}
.sym-list>li{position:relative;padding-left:14px;line-height:22.4px;color:var(--link-blue)}
.sym-list>li::before{content:"»";position:absolute;left:0;top:0;font-weight:700;color:var(--link-blue)}
.sym-list ul{list-style:none}
.sym-list ul>li{position:relative;padding-left:11px;color:#555;line-height:22.4px}
.sym-list ul>li::before{content:"▸";position:absolute;left:0;color:#666;font-size:8px}
.sym-list ul ul>li{font-size:8.5px;color:#8a8a8a;line-height:22px;padding-left:10px}
.sym-list ul ul>li::before{content:"•";font-size:8px;color:#aaa}
.sym-list .lvl2{margin-left:1px}
.sym-list .lvl3{margin:4px 0 6px 0}
.article h3{font-weight:400;font-size:13px;color:var(--heading-purple);margin:0 0 6px}
.grey-link{color:var(--link-grey);text-decoration:underline}
.refs-bar{margin-top:30px;height:24px;background:#e9e9e9;border-bottom:1px solid #ccc;display:flex;align-items:center;gap:8px;padding-left:8px;font-size:9.5px;font-weight:600;color:#333}
.refs-bar i{width:10px;height:10px;background:#999;color:#fff;font-style:normal;font-size:8px;line-height:10px;text-align:center}
.refs{list-style:none;font-size:9.5px;line-height:17.6px}
.refs li{display:flex;gap:10px;padding:9px 0 6px 8px;border-bottom:1px solid var(--rule)}

/* sidebar */
.tools{left:11px;top:12px;width:270px;height:33px;background:#fff;border:1px solid #8fa0c8;border-radius:3px;display:flex;gap:8px;padding:8px 8px}
.tools span{height:17px;background:linear-gradient(#fafafa,#e2e2e2);border:1px solid #bbb;border-radius:2px;font-family:"Arimo",sans-serif;font-size:7.5px;padding:0 8px;display:flex;align-items:center}
.info{left:12px;top:56px;width:268px;height:90px;background:#f1f1f1}
.info .hd{height:28px;background:var(--panel-dark);color:#fff;font-family:"Arimo",sans-serif;font-weight:700;font-size:8.5px;padding:8px 12px}
.info .row{margin:7px 8px 0;height:19px;background:#fff;font-family:"Arimo",sans-serif;font-size:7.5px;padding:5px 8px;color:#333}
.info .row a{text-decoration:underline}
.app-ad{left:36px;top:157px;width:221px;height:183px;background:#0d0d0d;border:1px solid #444}
.app-ad .hd{height:30px;background:#4a3170;color:#fff;font-family:"Arimo",sans-serif;font-size:14px;padding:6px 14px}
.app-ad .shots{left:10px;top:52px;width:200px;height:44px;background:linear-gradient(90deg,#3a3a3a,#8a8a8a 50%,#3a3a3a)}
.app-ad .line{left:0;top:128px;width:100%;text-align:center;color:#fff;font-family:"Arimo",sans-serif;font-size:9px}
.app-ad .btn{left:24px;top:150px;width:171px;height:22px;background:var(--orange);border-radius:3px;color:#8a3a05;font-family:"Arimo",sans-serif;font-size:7.5px;font-weight:700;display:flex;align-items:center;justify-content:center}
.case{width:131px;height:162px;background:#000;border:1px solid #666}
.case .scan{position:absolute;left:8px;top:6px;width:113px;height:118px;border-radius:48%;background:radial-gradient(#8a8a8a,#3a3a3a 70%,#000)}
.case .cap{position:absolute;left:0;bottom:0;width:100%;height:32px;background:rgba(60,60,60,.85);color:#fff;font-family:"Arimo",sans-serif;font-size:7.5px;line-height:9px;padding:6px 7px}

/* footer */
.promo{left:94px;top:1096px;width:535px;height:66px;background:linear-gradient(90deg,#26357a,#4b5cb0 60%,#2a3a80);border:1px solid #555}
.promo .big{left:13px;top:6px;color:#fff;font-family:"Arimo",sans-serif;font-weight:700;font-size:21px}
.promo .small{left:13px;top:36px;color:#fff;font-family:"Arimo",sans-serif;font-size:15px}
.promo .go{left:438px;top:20px;width:86px;height:24px;background:var(--orange);color:#fff;font-family:"Arimo",sans-serif;font-weight:700;font-size:8.5px;display:flex;align-items:center;justify-content:center;border-radius:2px}
.ver{right:26px;top:1150px;color:#ddd;font-family:"Arimo",sans-serif;font-size:10px}
.site-footer{left:0;top:1172px;width:726px;height:28px;background:#16191b;border-top:1px solid #333;font-family:"Arimo",sans-serif;font-weight:700;font-size:8.5px;color:#fff}
.site-footer span{position:absolute;top:9px}
</style>
</head>
<body>
<header class="site-header abs">
  <div class="brand abs"><span class="mark"></span>Corvantia.org</div>
  <div class="network abs">Member of the <span class="mark"></span> Halvern Medica network</div>
  <div class="account abs">Log in &nbsp;| Sign up</div>
  <div class="ad-banner abs">
    <div class="co abs">KESTREL</div>
    <div class="tag abs">Leading Innovation »</div>
    <div class="art abs" role="img" aria-label="Illustrated human figure showing scan dose map"></div>
    <div class="head abs">NEW DOSE<br>TRACKING SYSTEM</div>
    <div class="sub abs">Just one of Kestrel's 41 dose saving features available</div>
    <div class="cta abs">Click here to get the full story</div>
  </div>
  <div class="ads-note abs">About these ads</div>
  <nav class="main-nav abs">
    <div class="tab" style="width:110px"><b>ENCYCLOPEDIA</b><small>(Browse by topic or system)</small></div>
    <div class="tab act" style="width:68px"><i>+</i>Add<br>Article</div>
    <div class="tab gap"></div>
    <div class="tab" style="width:111px"><b>PATIENT CASES</b><small>(Browse by topic or system)</small></div>
    <div class="tab act" style="width:69px"><i>+</i>Add<br>Case</div>
    <div class="tab act" style="width:67px"><i>?</i>Quiz<br>Mode</div>
  </nav>
  <div class="search abs"><span></span><b>Search</b></div>
</header>

<main class="article abs">
  <div class="article-inner">
    <h1>Neurosarcoidosis</h1>
    <div class="byline">Dr Marcus Hale and Dr Simon Ferris et al.</div>
    <hr>
    <h2>Evolution through gestation</h2>
    <p class="lead">Although the myocardium begins to contract rhythmically by 3 weeks following-conception (from spontaneously depolarising myocardial pacemaker cells in the embryonic heart) it is first visible on sonography ~ 6 weeks of gestation where is usually around 100-120 beats per minute (bpm).</p>
    <p>The demographics of affected patients is not different to that of systemic sarcoidosis, typically affecting patients 30-40 years of age with a female predilection 2. Histologically, central nervous system involvement is seen in 14-27% of patients with systemic sarcoidosis, although only 3-15% are symptomatic 1-3. Interestingly up to 10% of patients with systemic disease will demonstrate imaging findings; thus not all patients with demon-</p>
    <p style="margin-top:12px">This then <strong>increases</strong> progressively over the subsequent 2-3 weeks becoming <sup>7</sup></p>
    <ul class="sym-list">
      <li>signs and symptoms of raised ICP due to hydrocephalus</li>
      <li>cranial nerve palsies
        <ul class="lvl2">
          <li>optic nerve involvement (particularly common) 5</li>
          <li>facial nerve palsy
            <ul class="lvl3">
              <li>Praesent neque dolor, fermentum quis facilisis quis, posuere ac ante.</li>
              <li>Duis ligula orci, cursus vitae ligula vel, iaculis congue tellus</li>
              <li>Maecenas dictum lacus ac ornare ultrices</li>
            </ul>
          </li>
        </ul>
      </li>
      <li>diabetes insipidus from pituitary involvement</li>
      <li>seizures</li>
      <li>variable weakness, paresthesias and dysarthria / dysphasia</li>
      <li>spinal cord involvement presenting as myelopathy <sup>5</sup></li>
    </ul>
    <hr style="margin:38px 0 14px">
    <h3>Pachymeningeal involvement</h3>
    <p>Pachymeningeal disease often takes the form of <a class="grey-link">pachymeningeal thickening</a> with homogenous <a>enhancement</a>. In some cases the masses can be low on T2 weighted images, which although a helpful clue, is not pathognomonic.</p>
    <div class="refs-bar"><i>+</i>References</div>
    <ol class="refs">
      <li><span>1.</span><span>Ravel P. The Golden S sign. Imaging Review. 2004;233 (3): 790-1.<br><a>doi:10.5550/imrev.4471208316 - MedIndex citation</a></span></li>
      <li><span>2.</span><span>Dalton J, Marsh EJ. Chest radiology, the essentials. Ashford Whitley &amp; Lane. (2007) ISBN:0000123456. <a>Read it at Folio Books - Find it at Bookery</a></span></li>
    </ol>
  </div>
</main>

<aside class="sidebar abs">
  <div class="tools abs"><span>✎ Edit Article</span><span>Share ▾</span><span>⚙ ▾</span></div>
  <div class="info abs">
    <div class="hd">Article Information:</div>
    <div class="row"><b>System:</b> <a>Central Nervous System</a></div>
    <div class="row">Tag: <a>oncology</a></div>
  </div>
  <div class="app-ad abs">
    <div class="hd">Corvantia.org mobile app</div>
    <div class="shots abs" role="img" aria-label="Three axial CT scan screenshots"></div>
    <div class="line abs">New case packs every month</div>
    <div class="btn abs">CLICK TO FIND OUT MORE</div>
  </div>
  <div class="case abs" style="left:12px;top:352px"><div class="scan" role="img" aria-label="Axial MRI of posterior fossa"></div><div class="cap">Case 1 : with leptomeningeal involvement</div></div>
  <div class="case abs" style="left:151px;top:352px"><div class="scan" role="img" aria-label="Coronal contrast MRI of brain"></div><div class="cap">Case 2 : with parenchymal involvement</div></div>
  <div class="case abs" style="left:12px;top:525px"><div class="scan" role="img" aria-label="Axial MRI of brain"></div><div class="cap">Case 3</div></div>
  <div class="case abs" style="left:151px;top:525px"><div class="scan" role="img" aria-label="Axial contrast MRI around pituitary stalk"></div><div class="cap">Case 4 : around pituitary stalk</div></div>
  <div class="case abs" style="left:12px;top:698px"><div class="scan" style="border-radius:30%;width:60px;left:36px" role="img" aria-label="Sagittal MRI of cervical spine"></div><div class="cap">Case 5: spinal cord involvement</div></div>
</aside>

<div class="promo abs">
  <div class="big abs">With over 12,000 cases</div>
  <div class="small abs">Isn't it time you started... 'cos it will take you some time....</div>
  <div class="go abs">GET STARTED</div>
</div>
<div class="ver abs">M2</div>
<footer class="site-footer abs">
  <span style="left:17px">Encyclopaedia</span>
  <span style="left:377px">Patient Cases</span>
  <span style="right:8px">About Corvantia.org</span>
</footer>
</body>
</html>
```